Design some Business Cards for Bright Harbour Advisory

I'm looking for a business card.
Business name - Bright Harbour Advisory (logo attached)
Details:
Dane Whitlock
dane@homestepsupport.com.au
0491 273 518
I want it to look simple and professional

```html
<!DOCTYPE html>
<html lang="en">
<head>
<meta charset="utf-8">
<title>Bright Harbour Advisory – Business Cards</title>
<link rel="stylesheet" href="https://fonts.googleapis.com/css2?family=Lato:wght@400;700&display=swap">
<style>
  :root {
    --page: #e9eaec;
    --card: #fbfbfb;
    --green: #8cc152;
    --blue: #3f95d6;
    --ink: #3c3c3c;
    --muted: #6a6a6a;
    --wordmark: #4a4a4a;
  }
  * { box-sizing: border-box; margin: 0; padding: 0; }
  html, body {
    width: 1200px; height: 800px; overflow: hidden;
    background: var(--page);
    font-family: "Lato", sans-serif;
  }
  .sheet {
    width: 1200px; height: 800px;
    display: flex; align-items: center; justify-content: center; gap: 60px;
  }
  .card {
    position: relative;
    width: 520px; height: 297px;
    background: var(--card);
    box-shadow: 0 6px 18px rgba(0,0,0,0.12);
    overflow: hidden;
  }
  .card__edge { position: absolute; left: 0; top: 0; width: 60px; height: 297px; }
  .wordmark {
    position: absolute;
    display: flex; align-items: center; gap: 10px;
    color: var(--wordmark);
    font-weight: 700;
    letter-spacing: 0.5px;
  }
  .wordmark__mark { width: 12px; height: 12px; background: var(--green); }
  .card--front .wordmark { top: 62px; right: 34px; font-size: 19px; }
  .card--back .wordmark { top: 128px; left: 78px; font-size: 26px; }
  .card--back .wordmark__mark { width: 16px; height: 16px; }
  .person { position: absolute; left: 70px; top: 112px; }
  .person__name { color: var(--blue); font-size: 24px; font-weight: 400; }
  .person__role { color: var(--muted); font-size: 11px; margin-top: 3px; }
  .contacts { position: absolute; left: 70px; top: 182px; list-style: none; }
  .contacts li {
    display: flex; align-items: center; gap: 12px;
    font-size: 10.5px; color: var(--ink); height: 30px;
  }
  .contacts__icon {
    width: 20px; height: 20px; background: var(--blue);
    display: flex; align-items: center; justify-content: center;
  }
</style>
</head>
<body>
<main class="sheet">
  <section class="card card--front" aria-label="Card front">
    <svg class="card__edge" viewBox="0 0 60 297" aria-hidden="true">
      <polygon points="0,0 54,0 32,38 0,62" fill="var(--blue)"/>
      <polygon points="0,70 32,46 32,297 0,297" fill="var(--green)"/>
    </svg>
    <div class="wordmark"><span class="wordmark__mark"></span>Bright Harbour Advisory</div>
    <div class="person">
      <h1 class="person__name">Dane Whitlock</h1>
      <p class="person__role">Landscape Advisor</p>
    </div>
    <ul class="contacts">
      <li>
        <span class="contacts__icon">
          <svg width="12" height="10" viewBox="0 0 12 10" aria-hidden="true"><rect x="0.5" y="0.5" width="11" height="9" fill="none" stroke="#fff"/><polyline points="0.5,0.5 6,5.5 11.5,0.5" fill="none" stroke="#fff"/></svg>
        </span>dane@homestepsupport.com.au
      </li>
      <li>
        <span class="contacts__icon">
          <svg width="12" height="12" viewBox="0 0 12 12" aria-hidden="true"><circle cx="6" cy="6" r="5" fill="none" stroke="#fff"/><ellipse cx="6" cy="6" rx="2.2" ry="5" fill="none" stroke="#fff"/><line x1="1" y1="6" x2="11" y2="6" stroke="#fff"/></svg>
        </span>www.homestepsupport.com.au
      </li>
      <li>
        <span class="contacts__icon">
          <svg width="10" height="12" viewBox="0 0 10 12" aria-hidden="true"><path d="M2 0.5 L4 3.5 L3 5 Q4.5 7.5 6 8.5 L7.5 7.5 L9.5 9.5 L8 11.5 Q3.5 10.5 0.5 3 Z" fill="#fff"/></svg>
        </span>0491 273 518
      </li>
    </ul>
  </section>

  <section class="card card--back" aria-label="Card back">
    <svg class="card__edge" viewBox="0 0 60 297" aria-hidden="true">
      <polygon points="0,0 54,0 32,38 0,62" fill="var(--blue)"/>
      <polygon points="0,70 32,46 32,297 0,297" fill="var(--green)"/>
    </svg>
    <div class="wordmark"><span class="wordmark__mark"></span>Bright Harbour Advisory</div>
  </section>
</main>
</body>
</html>
```